Lanyard that Pops with our URL and Product Name

We need a design with our logo and URL for a lanyard to wear at trade shows and events. We are looking for something more than just a person sticking our logo and URL on the lanyard and calling it good. We want something that POPS when folks look at it and see it is different. Edgy. Hip. Modern. Attention Grabbing

- Winner will have opportunity to create a new biz card as well. Biz card should bd double sided. For some reason, Artmarketly keeps reverting it back to single-side.

Contact Information for Business Card

Dorian Plessy, CEO
TrovaEdPath
e: dorian.plessy@dorianplessygrp.example
p: 603.419.2286

Colors

Designer to choose colors to be used in the design.

Requirements
Must have
• The words Search. Compare. Engage. (as the tag line to TrovaEdPath)
• The URL trovaedpath.example
• On the back social icons with the link
• Chirpline: @marlowatdesk
• Netlinkpro: https://www.netlinkpro.example/in/dorianplessyinsf
• Blog: https://skillnotes365.example
Should not have
• Bland look to it.

```html
<!DOCTYPE html>
<html lang="en">
<head>
<meta charset="utf-8">
<title>TrovaEdPath business card</title>
<link rel="stylesheet" href="https://fonts.googleapis.com/css2?family=Raleway:wght@400;500;600;800&display=swap">
<style>
  :root {
    --bg: #e4e4e4;
    --card: #283552;
    --card-deep: #222d47;
    --brand-blue: #1b90d4;
    --band-blue: #1f9ad9;
    --band-light: #5cc0ee;
    --text: #ffffff;
    --text-soft: #c9d3e4;
    --pill: #34456a;
  }
  * { box-sizing: border-box; margin: 0; padding: 0; }
  html, body { width: 1200px; height: 852px; overflow: hidden; }
  body {
    background: var(--bg);
    font-family: "Raleway", sans-serif;
    color: var(--text);
    position: relative;
  }
  .card {
    position: absolute;
    width: 500px;
    height: 290px;
    border-radius: 22px;
    background: var(--card);
    overflow: hidden;
    box-shadow: 0 6px 14px rgba(0,0,0,0.25);
  }
  .card--front { left: 70px; top: 281px; }
  .card--back { left: 630px; top: 281px; }

  .brand { position: absolute; display: flex; align-items: center; gap: 12px; }
  .brand__mark {
    width: 34px; height: 34px; border-radius: 50%;
    background: var(--brand-blue);
  }
  .brand__name {
    font-weight: 800; color: var(--brand-blue); line-height: 1;
  }
  .brand__tagline {
    font-weight: 600; color: var(--text); margin-top: 3px;
  }
  .card--front .brand { left: 70px; top: 92px; }
  .card--front .brand__name { font-size: 40px; }
  .card--front .brand__tagline { font-size: 14px; }

  .url-pill {
    position: absolute; left: 155px; top: 190px;
    width: 210px; height: 32px; border-radius: 16px;
    background: var(--pill);
    border: 1px solid var(--brand-blue);
    box-shadow: inset 0 2px 4px rgba(0,0,0,0.35);
    display: flex; align-items: center; justify-content: center;
    font-size: 13px; font-weight: 500;
  }
  .url-pill__accent { color: var(--brand-blue); }
  .url-pill__cursor { position: absolute; right: -10px; top: -12px; }

  .card--back .brand { left: 28px; top: 40px; }
  .card--back .brand__mark { width: 28px; height: 28px; }
  .card--back .brand__name { font-size: 30px; }
  .card--back .brand__tagline { font-size: 11px; }

  .faint-disc {
    position: absolute; right: 40px; top: -40px;
    width: 170px; height: 170px; border-radius: 50%;
    background: rgba(255,255,255,0.05);
  }
  .person { position: absolute; left: 40px; top: 132px; }
  .person__name { font-size: 22px; font-weight: 600; }
  .person__title { font-size: 12px; color: var(--text-soft); margin-top: 2px; }

  .contact { position: absolute; left: 40px; top: 200px; list-style: none; }
  .contact li, .social li {
    display: flex; align-items: center; gap: 8px;
    font-size: 12.5px; line-height: 19px; color: var(--text-soft);
  }
  .contact svg { flex: none; }

  .social { position: absolute; right: 26px; top: 112px; list-style: none; }
  .social__dot {
    width: 11px; height: 11px; border-radius: 50%;
    background: var(--text-soft); flex: none;
  }

  .band { position: absolute; left: 0; bottom: 0; }
  .tagline-tab {
    position: absolute; right: 0; bottom: 18px;
    width: 225px; height: 56px;
    display: flex; align-items: center; justify-content: center;
    font-size: 13px; font-weight: 500; color: var(--text);
    letter-spacing: 0.2px;
  }
  .tagline-tab span { opacity: 0.8; margin: 0 7px; }
</style>
</head>
<body>

<section class="card card--front" aria-label="Card front">
  <div class="brand">
    <div class="brand__mark"></div>
    <div>
      <div class="brand__name">TrovaEdPath</div>
      <div class="brand__tagline">Finding the right LMS for you.</div>
    </div>
  </div>
  <div class="url-pill">
    www.<span class="url-pill__accent">trovaedpath</span>.example
    <svg class="url-pill__cursor" width="18" height="20" viewBox="0 0 18 20">
      <path d="M3 2 L3 16 L7 12 L10 18 L12 17 L9 11 L15 11 Z" fill="#ffffff" stroke="#222d47" stroke-width="1"/>
    </svg>
  </div>
</section>

<section class="card card--back" aria-label="Card back">
  <div class="faint-disc"></div>

  <div class="brand">
    <div class="brand__mark"></div>
    <div>
      <div class="brand__name">TrovaEdPath</div>
      <div class="brand__tagline">Finding the right LMS for you.</div>
    </div>
  </div>

  <ul class="social">
    <li><span class="social__dot"></span>@marlowatdesk</li>
    <li><span class="social__dot"></span>/dorianplessyinsf</li>
    <li><span class="social__dot"></span>skillnotes365.example</li>
  </ul>

  <div class="person">
    <div class="person__name">Dorian Plessy</div>
    <div class="person__title">Managing Director</div>
  </div>

  <ul class="contact">
    <li>
      <svg width="12" height="12" viewBox="0 0 12 12"><path d="M2 1 L4.5 1 L5.5 3.5 L4 4.5 Q5 7 7.5 8 L8.5 6.5 L11 7.5 L11 10 Q6 11 2 6 Q1 3 2 1Z" fill="#c9d3e4"/></svg>
      1-603-419-2286
    </li>
    <li>
      <svg width="12" height="12" viewBox="0 0 12 12"><rect x="0.5" y="2.5" width="11" height="7" fill="none" stroke="#c9d3e4"/><path d="M0.5 2.5 L6 7 L11.5 2.5" fill="none" stroke="#c9d3e4"/></svg>
      dorian@trovaedpath.example
    </li>
    <li>
      <svg width="12" height="12" viewBox="0 0 12 12"><circle cx="6" cy="6" r="5" fill="none" stroke="#c9d3e4"/><ellipse cx="6" cy="6" rx="2.2" ry="5" fill="none" stroke="#c9d3e4"/><line x1="1" y1="6" x2="11" y2="6" stroke="#c9d3e4"/></svg>
      www.trovaedpath.example
    </li>
  </ul>

  <svg class="band" width="500" height="80" viewBox="0 0 500 80">
    <path d="M0 72 L250 62 Q270 61 275 50 L282 30 Q287 22 300 22 L500 22 L500 80 L0 80 Z" fill="#1f9ad9"/>
    <path d="M0 72 L250 62 Q270 61 275 50 L278 42 L272 68 L0 78 Z" fill="#5cc0ee" opacity="0.6"/>
  </svg>
  <div class="tagline-tab">Search<span>|</span>Compare<span>|</span>Engage</div>
</section>

</body>
</html>
```